Letterhead design - Ferrowby Group

We have just had our Logo created and our now wantng a letterhead design to incorporate this. Please use the same colours as in the logo, which is attached.
Please use the company details below
P O Box 86, Bleneheim 7240
Ph: 03 491 2753
dale@ferrowbygroup.co.nz
We would like a professional look
We need an overall letterhead design for our varied group of buisinesses which are based in NZ and overseas. We grow and develop buisinesses. Our companies began in NZ but we now have branches overseas as well. People are our greatest asset and we employ some incredible staff. Our buisinesses are scientific, innovative and growing in size and expertise with a financial base.

Target Market(s)

Professionals

Industry/Entity Type

Investment

Requirements
Must have
• Easy to read.
• Please use the same colours as in the logo
• Please use the company details below
• P O Box 86, Bleneheim 7240
• Ph: 03 491 2753
• dale@ferrowbygroup.co.nz

```html
<!DOCTYPE html>
<html lang="en">
<head>
<meta charset="utf-8">
<title>Ferrowby Group Letterhead</title>
<link rel="stylesheet" href="https://fonts.googleapis.com/css2?family=Source+Sans+3:wght@400;600&family=Kristi&display=swap">
<style>
  :root {
    --brand-green: #10b46a;
    --ink: #3f3f3f;
    --ink-soft: #555555;
    --rule-grey: #a9a9a9;
    --rule-dark: #5a5a5a;
    --mark-grey: #4a4a4a;
    --paper: #ffffff;
    --backdrop: #ecebe8;
  }
  * { margin: 0; padding: 0; box-sizing: border-box; }
  html, body {
    width: 1112px; height: 1200px; overflow: hidden;
    background: var(--backdrop);
  }
  body { position: relative; font-family: "Source Sans 3", Arial, sans-serif; color: var(--ink); }
  .letterhead {
    position: absolute; left: 213px; top: 89px;
    width: 701px; height: 990px;
    background: var(--paper);
  }
  .brand {
    position: absolute; left: 62px; top: 37px;
    display: flex; align-items: center; gap: 12px;
  }
  .brand-square { width: 44px; height: 44px; background: var(--mark-grey); }
  .brand-name {
    font-weight: 600; font-size: 27px; color: var(--brand-green);
    letter-spacing: 0.2px; line-height: 1;
  }
  .contact {
    position: absolute; left: 444px; top: 41px;
    font-size: 14px; line-height: 18px; color: var(--ink-soft);
  }
  .contact-item { display: flex; align-items: center; gap: 6px; }
  .contact-item svg { width: 14px; height: 14px; flex: none; }
  .header-rule { position: absolute; left: 0; top: 110px; width: 701px; height: 10px; }
  .recipient {
    position: absolute; left: 61px; top: 219px;
    font-size: 15px; line-height: 20px; color: var(--ink);
  }
  .letter-date {
    position: absolute; right: 61px; top: 219px;
    font-size: 15px; line-height: 20px; color: var(--ink);
  }
  .letter-body {
    position: absolute; left: 61px; top: 318px; width: 579px;
    font-size: 14px; line-height: 18.3px; color: var(--ink-soft);
    text-align: justify;
  }
  .letter-body p { margin-bottom: 18.5px; }
  .signoff {
    position: absolute; right: 61px; top: 790px; text-align: right;
  }
  .signoff-name {
    font-family: "Kristi", cursive; font-size: 36px; line-height: 36px; color: #222;
  }
  .signoff-title { font-size: 14px; color: var(--ink); margin-top: 2px; }
  .footer-rule { position: absolute; left: 0; top: 944px; width: 701px; height: 10px; }
  .footer {
    position: absolute; left: 0; top: 938px; width: 701px;
    text-align: center; font-size: 14px; line-height: 17px; color: var(--ink-soft);
  }
  .footer-name { font-weight: 600; }
  .footer-name .accent { color: var(--brand-green); }
</style>
</head>
<body>
  <main class="letterhead">
    <div class="brand">
      <span class="brand-square"></span>
      <span class="brand-name">Ferrowby Group</span>
    </div>

    <div class="contact">
      <div class="contact-item">
        <svg viewBox="0 0 14 14" aria-hidden="true">
          <circle cx="7" cy="7" r="7" fill="var(--brand-green)"/>
          <path d="M4.6 3.6l1.3 1.4-.7 1c.5 1 1.2 1.7 2.2 2.2l1-.7 1.4 1.3-.8 1.1C6.6 9.7 4.3 7.4 3.9 4.4z" fill="#fff"/>
        </svg>
        <span>03 491 2753</span>
      </div>
      <div class="contact-item">
        <svg viewBox="0 0 14 14" aria-hidden="true">
          <circle cx="7" cy="7" r="7" fill="var(--brand-green)"/>
          <rect x="3.5" y="4.5" width="7" height="5" fill="none" stroke="#fff" stroke-width="1"/>
          <path d="M3.5 4.5L7 7.3l3.5-2.8" fill="none" stroke="#fff" stroke-width="1"/>
        </svg>
        <span>dale@ferrowbygroup.co.nz</span>
      </div>
    </div>

    <svg class="header-rule" viewBox="0 0 701 10" aria-hidden="true">
      <line x1="0" y1="8.5" x2="701" y2="8.5" stroke="var(--rule-grey)" stroke-width="1"/>
      <polygon points="0,2 279,2 284,9 0,9" fill="var(--brand-green)"/>
    </svg>

    <div class="recipient">
      <div>Recipient's Name</div>
      <div>Recipient's Title</div>
      <div>Recipient's Company</div>
      <div>Recipient's Company Address</div>
    </div>
    <div class="letter-date">Ankerrul January, 2016</div>

    <div class="letter-body">
      <p>Lorem Ipsum is simply dummy text of the printing and typesetting industry. Lorem Ipsum has been the industry's standard dummy text ever since the 1500s, when an unknown printer took a galley of type and scrambled it to make a type specimen book. It has survived not only five centuries, but also the leap into electronic typesetting, remaining essentially unchanged. It was popularised in the 1960s with the release of Pressfast sheets containing Lorem Ipsum passages, and more recently with desktop publishing software like Quillset Composer including versions of Lorem Ipsum.</p>
      <p>The standard chunk of Lorem Ipsum used since the 1500s is reproduced below for those interested. Sections 1.10.32 and 1.10.33 from "de Finibus Bonorum et Malorum" by Aurelian are also reproduced in their exact original form, accompanied by English versions from the 1914 translation by J. Wendell</p>
      <p>Lorem Ipsum is simply dummy text of the printing and typesetting industry. Lorem Ipsum has been the industry's standard dummy text ever since the 1500s, when an unknown printer took a galley of type and scrambled it to make a type specimen book. It has survived not only five centuries, but also the leap into electronic typesetting, remaining essentially unchanged. It was popularised in the</p>
      <p>The standard chunk of Lorem Ipsum used since the 1500s is reproduced below for those interested. Sections 1.10.32 and 1.10.33 from "de Finibus Bonorum et Malorum" by Aurelian are also reproduced in their exact original form, accompanied by English versions from the 1914 translation by J. Wendell.</p>
    </div>

    <div class="signoff">
      <div class="signoff-name">your name</div>
      <div class="signoff-title">Company Director</div>
    </div>

    <svg class="footer-rule" viewBox="0 0 701 10" aria-hidden="true">
      <line x1="0" y1="5" x2="278" y2="5" stroke="var(--rule-grey)" stroke-width="1"/>
      <line x1="416" y1="5" x2="701" y2="5" stroke="var(--rule-grey)" stroke-width="1"/>
      <line x1="0" y1="5" x2="22" y2="5" stroke="var(--rule-dark)" stroke-width="2"/>
      <line x1="678" y1="5" x2="701" y2="5" stroke="var(--rule-dark)" stroke-width="2"/>
    </svg>
    <div class="footer">
      <div class="footer-name"><span class="accent">Ferrowby</span> Group</div>
      <div class="footer-address">P O Box 86, Bleneheim 7240</div>
    </div>
  </main>
</body>
</html>
```